Tri-fold Brochure for Law Firm

Double-sided brochure to be folded into 6 sides tri-fold brochure for an estate planning special for new parents or parents-to-be. Brochure will be placed in classes for new parents/young parents.

Target Market(s)

New Parents Aged 24-34

Industry/Entity Type

Law Firm

Font styles to use
Serif

Requirements
Must have
• The information provided in the word document.
Nice to have
• Highlight the phrase "for New Parents."
• You may use the color scheme from our website:
• http://k47.9dw.sitevaultexample.com/

```html
<!DOCTYPE html>
<html lang="en">
<head>
<meta charset="utf-8">
<title>Harlow Legal – Estate Planning Special Brochure</title>
<link href="https://fonts.googleapis.com/css2?family=Roboto+Condensed:wght@400;700&family=Open+Sans:ital,wght@0,400;0,600;0,700;1,400&display=swap" rel="stylesheet">
<style>
  :root {
    --gold: #f2ae0f;
    --gold-deep: #e39b05;
    --charcoal: #3c3c3e;
    --ink: #2b2b2b;
    --paper: #ffffff;
    --mist: #eef0f2;
    --stage-top: #9a9697;
    --stage-bottom: #6f6b6c;
  }
  * { box-sizing: border-box; margin: 0; padding: 0; }
  html, body { width: 1200px; height: 1200px; overflow: hidden; }
  body {
    background: linear-gradient(180deg, var(--stage-top), var(--stage-bottom));
    font-family: "Open Sans", Arial, sans-serif;
    color: var(--ink);
  }
  .brochure {
    position: absolute; left: 30px; top: 170px;
    width: 1140px; height: 860px;
    display: flex;
    box-shadow: 0 14px 40px rgba(0,0,0,.35);
  }
  .panel {
    position: relative; width: 380px; height: 860px;
    background: var(--paper); overflow: hidden;
  }
  .panel + .panel { border-left: 1px solid rgba(0,0,0,.06); }
  .panel-bg { position: absolute; inset: 0; width: 100%; height: 100%; }
  .headline { font-family: "Roboto Condensed", Arial, sans-serif; }

  /* inside flap */
  .audience { position: absolute; left: 40px; top: 36px; width: 310px; line-height: 1.05; }
  .audience .lead { font-size: 34px; color: var(--ink); }
  .audience .accent { font-size: 34px; font-weight: 700; color: var(--gold); }
  .audience .price { font-size: 17px; font-weight: 700; color: var(--gold); margin-top: 6px; }
  .for-label { position: absolute; left: 0; width: 100%; top: 305px; text-align: center; font-size: 26px; color: var(--ink); }
  .why { position: absolute; left: 36px; top: 360px; width: 310px; font-size: 11.5px; line-height: 1.55; color: #555; }
  .why h2 { font-size: 13px; font-weight: 700; color: var(--gold); margin-bottom: 8px; }
  .why p { margin-bottom: 10px; }
  .why blockquote { font-style: italic; margin-top: 14px; }
  .why cite { display: block; font-style: normal; font-weight: 600; color: var(--gold); margin-top: 4px; }
  .web { position: absolute; left: 0; width: 100%; bottom: 28px; text-align: center; font-size: 14px; font-weight: 700; letter-spacing: 3px; color: var(--ink); }

  /* contact panel */
  .portrait, .map {
    position: absolute; border-radius: 50%;
  }
  .portrait {
    left: 115px; top: 95px; width: 170px; height: 170px;
    border: 9px solid var(--charcoal);
    background: radial-gradient(circle at 50% 40%, #b88c7a, #5a2f2a 70%);
  }
  .map {
    left: 105px; top: 285px; width: 130px; height: 130px;
    border: 5px solid var(--charcoal);
    background: linear-gradient(135deg, #e9e9e9, #d3d5d8);
  }
  .contact { position: absolute; left: 72px; top: 470px; width: 290px; color: var(--ink); }
  .contact .firm { font-size: 16px; font-weight: 700; margin-bottom: 10px; }
  .contact ul { list-style: none; }
  .contact li { position: relative; padding-left: 18px; font-size: 13px; line-height: 1.5; margin-bottom: 4px; }
  .contact li::before { content: ""; position: absolute; left: 0; top: 7px; width: 7px; height: 7px; border-radius: 50%; background: var(--paper); }
  .contact .phone-main { font-family: "Roboto Condensed", Arial, sans-serif; font-size: 28px; font-weight: 700; line-height: 1.1; }
  .contact .phone-main::before { top: 13px; }

  /* cover */
  .brand { position: absolute; left: 0; width: 100%; top: 28px; text-align: center; }
  .brand .dot { display: block; width: 26px; height: 26px; border-radius: 50%; background: var(--gold); margin: 0 auto 8px; }
  .brand .name { font-size: 14px; font-weight: 700; color: var(--ink); letter-spacing: .5px; }
  .cover-photo {
    position: absolute; left: 0; top: 110px; width: 380px; height: 340px;
    background: linear-gradient(160deg, #e7ecf0 0%, #b9c0c7 45%, #3b3f48 100%);
    clip-path: path("M0,0 H380 V300 C250,330 120,300 0,250 Z");
  }
  .offer { position: absolute; left: 36px; top: 520px; width: 320px; }
  .offer .line1 { font-size: 38px; color: var(--ink); line-height: 1; }
  .offer .line2 { font-size: 82px; font-weight: 700; color: var(--gold); line-height: .95; }
  .offer .line3 { font-size: 36px; font-weight: 700; color: var(--ink); line-height: 1; }
</style>
</head>
<body>
<main class="brochure">

  <!-- Inside flap -->
  <section class="panel panel-flap">
    <svg class="panel-bg" viewBox="0 0 380 860" aria-hidden="true">
      <path d="M0,250 C120,300 260,230 380,150 L380,185 C260,265 120,330 0,285 Z" fill="var(--gold)"/>
      <path d="M0,292 C120,340 260,280 380,200 L380,222 C260,300 120,360 0,318 Z" fill="var(--charcoal)"/>
      <path d="M0,720 C140,690 260,720 380,760 L380,775 C260,740 140,710 0,738 Z" fill="var(--charcoal)"/>
      <path d="M0,748 C140,720 260,750 380,790 L380,860 L0,860 Z" fill="var(--gold)"/>
    </svg>
    <div class="audience headline">
      <div class="lead">For parents-to-be<br>and parents</div>
      <div class="accent">of children<br>Under 5 years old</div>
      <div class="price">$750 per couple</div>
    </div>
    <div class="for-label headline">FOR</div>
    <article class="why">
      <h2>Why should every parent have a will?</h2>
      <p>Imagine how many people love your children. Would there be a fight over who would care for your children if you passed away without leaving instructions?</p>
      <p>Naming a guardian in your will helps avoid litigation that would cause additional stress to your children and loved ones. You can also name a back-up in the event that your first choice is unable or unwilling to serve as guardian.</p>
      <blockquote>“I have seen first-hand the problems created when a parent dies without a will. Busy parents put off planning, yet having a plan is the most important gift for your children. I created this special to encourage new parents to start planning before it is too late.”
        <cite>Nora Harlow, Esq.</cite>
      </blockquote>
    </article>
    <div class="web">www.harlow-legal.example</div>
  </section>

  <!-- Contact panel -->
  <section class="panel panel-contact">
    <svg class="panel-bg" viewBox="0 0 380 860" aria-hidden="true">
      <rect width="380" height="300" fill="var(--mist)"/>
      <path d="M0,270 C110,300 250,230 380,170 L380,860 L0,860 Z" fill="var(--gold)"/>
      <path d="M0,775 C110,700 260,700 380,770 L380,860 L0,860 Z" fill="var(--paper)"/>
      <path d="M0,785 C110,712 260,712 380,782 L380,860 L0,860 Z" fill="var(--charcoal)"/>
    </svg>
    <div class="portrait" role="img" aria-label="Portrait photo of the attorney"></div>
    <div class="map" role="img" aria-label="Street map showing the office location"></div>
    <div class="contact">
      <div class="firm">HARLOW LEGAL, LLC</div>
      <ul>
        <li class="phone-main">(555)-014-3382</li>
        <li>48 Linden Avenue, Suite 310<br>Fairview, ST 00000</li>
        <li>(555)-018-2207</li>
        <li>nora@harlow-legal.example</li>
        <li>www.harlow-legal.example</li>
      </ul>
    </div>
  </section>

  <!-- Cover -->
  <section class="panel panel-cover">
    <svg class="panel-bg" viewBox="0 0 380 860" aria-hidden="true">
      <path d="M0,370 C120,420 250,440 380,410 L380,440 C250,470 120,455 0,400 Z" fill="var(--gold)"/>
      <path d="M0,410 C120,465 250,480 380,450 L380,475 C250,505 120,495 0,440 Z" fill="var(--charcoal)"/>
      <path d="M0,740 C130,770 260,770 380,745 L380,760 C260,790 130,790 0,758 Z" fill="var(--charcoal)"/>
      <path d="M0,770 C130,800 260,800 380,775 L380,860 L0,860 Z" fill="var(--gold)"/>
    </svg>
    <div class="brand">
      <span class="dot"></span>
      <span class="name">HARLOW LEGAL, LLC</span>
    </div>
    <div class="cover-photo" role="img" aria-label="Photo of an attorney reviewing documents with a client"></div>
    <h1 class="offer headline">
      <span class="line1">ESTATE PLANNING</span><br>
      <span class="line2">SPECIAL</span><br>
      <span class="line3">FOR NEW PARENTS</span>
    </h1>
    <div class="web">www.harlow-legal.example</div>
  </section>

</main>
</body>
</html>
```